Business Card Needed for Crafter of Pottery, Jewelry and Artwork

Calling all designers in search of an artistic challenge.

I need a new business card design for my pottery, jewelry and artwork business, Woven Glass and Tide, based in Vancouver BC.

I would like a card that is bright and inviting and preferably incorporates my logo and a sample of photos of my work while having a clean fresh look. The following contact details would preferably be included on the card as well:
• Helena Pikeworth
• Designer
• Phone: 604.555.0172
• Email: Designer@WovenGlassandTide.example
• Website: www.WovenGlassandTide.example
• Blog: www.ShapingHillside.example

The logo is attached in two color schemes in both Vector and Source formats. On past cards I’ve also included photos of my work. By including photos of the work the pieces are showcased and it catches people’s eye and prompts them to pick up the card and look at it more closely. For example, if I leave a stack in a coffee shop I want people to be drawn to the card, to pick it up and get a sense of the my product lines. Please feel free to pull photos of my work directly off of my website. If you need photos with higher pixels please let me know and I’ll email them directly to you. The website background is bffbda (191, 251, 218). I would like the business cards to match the feel of the website for consistency but the cards do not need to use the exact same colors. My website and current business card are predominantly turquoise shades. The background uses stripes provided by the website template. I don’t know the exact colors of the stripes.

My current business card is attached to show the use of photos in a design. Please note that I am not thrilled with my own design and am looking for variations and completely new designs. This example is not meant to be used as a template or starting point.

Here is some background surrounding my company:
WGT offers one of a kind jewelry, pottery, artwork and leather bags each designed with a twist. The pottery varies from rustic every day functional ware to raku artwork. The jewelry ranges from simple sterling every day pieces to multimedia pieces incorporating stone, metal, ceramics and fabric. The artwork is multimedia, typically acrylic paired with a natural element such as bark. All the bags are leather with reworked kimono fabric or patterned silk lining.

Feel free to check out my website to get a flavour for my work and the color scheme I've used on marketing materials so far. www.wovenglassandtide.example
Updates

Thank you to everyone who has submitted a design so far. I hope everyone has received some helpful feedback.

I'm going to post a survey to customers and friends asking for their votes. If you have new designs to submit please try to get them in by Saturday March 30 at noon so that I can include it in the survey launch.

Thank you

Target Market(s)

Females aged 25-65 interested in one of a kind functional pottery and jewelry.

Industry/Entity Type

Coffee Shop

Requirements
Must have
• Contact information, website, blog
Nice to have
• Logo, photos

```html
<!DOCTYPE html>
<html lang="en">
<head>
<meta charset="utf-8">
<title>Woven Glass and Tide — Business Card</title>
<link rel="stylesheet" href="https://fonts.googleapis.com/css2?family=Libre+Baskerville:wght@400;700&display=swap">
<style>
  :root {
    --page-bg: #ece8e1;
    --turquoise: #3fb2a6;
    --turquoise-ring: #e6f4f2;
    --navy: #232a6e;
    --card-white: #ffffff;
    --ink: #1c1c1c;
    --tile-frame: #f4f4f2;
    --flourish-tone: #d6d6d6;
  }
  * { box-sizing: border-box; margin: 0; padding: 0; }
  html, body {
    width: 1200px; height: 750px; overflow: hidden;
    background: var(--page-bg);
    font-family: "Libre Baskerville", Georgia, serif;
    color: var(--ink);
  }
  .stage {
    width: 1200px; height: 750px;
    display: flex; align-items: center; justify-content: center; gap: 40px;
  }
  .card {
    width: 540px; height: 310px; border-radius: 6px;
    box-shadow: 0 6px 18px rgba(0,0,0,.18);
    position: relative; overflow: hidden;
  }

  /* Front face: portfolio grid */
  .card-front { background: var(--turquoise); padding: 16px; }
  .portfolio-grid {
    display: grid; width: 100%; height: 100%;
    grid-template-columns: repeat(6, 1fr);
    grid-template-rows: repeat(3, 1fr);
    gap: 10px;
  }
  .work-tile { background: var(--tile-frame); padding: 6px; }
  .work-photo { width: 100%; height: 100%; }
  .badge {
    position: absolute; left: 50%; top: 50%;
    width: 156px; height: 156px; margin: -78px 0 0 -78px;
    border-radius: 50%; background: var(--turquoise);
    border: 6px solid var(--card-white);
    display: flex; align-items: center; justify-content: center; text-align: center;
    box-shadow: 0 2px 6px rgba(0,0,0,.2);
  }
  .badge-name {
    font-size: 17px; line-height: 1.3; font-weight: 700; color: var(--navy);
    letter-spacing: .04em;
  }

  /* Back face: contact */
  .card-back { background: var(--card-white); }
  .back-badge {
    position: absolute; left: 202px; top: 24px;
    width: 106px; height: 106px; border-radius: 50%;
    background: var(--turquoise); border: 4px solid var(--turquoise-ring);
    display: flex; align-items: center; justify-content: center; text-align: center;
  }
  .back-badge .badge-name { font-size: 12px; }
  .holder {
    position: absolute; left: 0; right: 0; top: 142px; text-align: center;
    padding-left: 30px;
  }
  .holder-name { font-size: 21px; font-weight: 700; letter-spacing: .12em; }
  .holder-role { font-size: 14px; letter-spacing: .1em; margin-top: 4px; }
  .divider-flourish {
    width: 58px; height: 12px; margin: 14px auto 0;
    background: var(--flourish-tone); border-radius: 6px;
  }
  .contact {
    position: absolute; left: 22px; right: 22px; bottom: 26px;
    display: flex; justify-content: space-between;
    font-size: 8.5px; letter-spacing: .06em; line-height: 1.9;
  }
  .contact-line b { display: inline-block; width: 16px; font-weight: 700; }
</style>
</head>
<body>
<main class="stage">
  <section class="card card-front" aria-label="Card front">
    <div class="portfolio-grid">
      <div class="work-tile"><div class="work-photo" role="img" aria-label="Photo of red leather bag" style="background:radial-gradient(circle at 50% 55%,#c94a3e 0 38%,#e8e4df 62%)"></div></div>
      <div class="work-tile"><div class="work-photo" role="img" aria-label="Photo of red bead necklace" style="background:radial-gradient(circle at 50% 50%,#c22a2a 0 30%,#ece9e4 60%)"></div></div>
      <div class="work-tile"><div class="work-photo" role="img" aria-label="Photo of teal fabric clutch" style="background:radial-gradient(circle at 50% 50%,#4f9896 0 36%,#e6e3de 62%)"></div></div>
      <div class="work-tile"><div class="work-photo" role="img" aria-label="Photo of wood and green stone necklace" style="background:radial-gradient(circle at 50% 50%,#8a5a36 0 28%,#ebe6dd 60%)"></div></div>
      <div class="work-tile"><div class="work-photo" role="img" aria-label="Photo of dark glazed bowl" style="background:radial-gradient(circle at 50% 50%,#2f3a42 0 36%,#dcd9d4 62%)"></div></div>
      <div class="work-tile"><div class="work-photo" role="img" aria-label="Photo of blue drop earrings" style="background:radial-gradient(circle at 50% 50%,#2f6a85 0 22%,#e4e4e4 55%)"></div></div>
      <div class="work-tile"><div class="work-photo" role="img" aria-label="Photo of green raku vase" style="background:radial-gradient(circle at 50% 55%,#3e5a48 0 36%,#dcdcd8 62%)"></div></div>
      <div class="work-tile"><div class="work-photo" role="img" aria-label="Photo of peacock feather earrings" style="background:radial-gradient(circle at 50% 50%,#3f6a63 0 26%,#dedcd6 58%)"></div></div>
      <div class="work-tile"><div class="work-photo" role="img" aria-label="Photo of wooden bowl" style="background:radial-gradient(circle at 50% 50%,#b58a5e 0 34%,#eeeeec 60%)"></div></div>
      <div class="work-tile"><div class="work-photo" role="img" aria-label="Photo of carved wooden bowl" style="background:radial-gradient(circle at 50% 50%,#a87c52 0 34%,#efede9 60%)"></div></div>
      <div class="work-tile"><div class="work-photo" role="img" aria-label="Photo of lidded green jar" style="background:radial-gradient(circle at 50% 50%,#6e7a55 0 34%,#e4e1da 62%)"></div></div>
      <div class="work-tile"><div class="work-photo" role="img" aria-label="Photo of sunset painting" style="background:linear-gradient(#e59a3a 0 55%,#c9563a 55% 75%,#efece6 75%)"></div></div>
      <div class="work-tile"><div class="work-photo" role="img" aria-label="Photo of ceramic owl" style="background:radial-gradient(circle at 50% 50%,#7b6448 0 36%,#e3e0da 62%)"></div></div>
      <div class="work-tile"><div class="work-photo" role="img" aria-label="Photo of glazed mugs" style="background:radial-gradient(circle at 50% 55%,#6b8a78 0 36%,#dcd8d0 62%)"></div></div>
      <div class="work-tile"><div class="work-photo" role="img" aria-label="Photo of stoneware cup" style="background:radial-gradient(circle at 50% 50%,#bfa88a 0 32%,#eeeeec 60%)"></div></div>
      <div class="work-tile"><div class="work-photo" role="img" aria-label="Photo of coral and teal bead earrings" style="background:radial-gradient(circle at 50% 50%,#c4604f 0 24%,#e6e6e4 56%)"></div></div>
      <div class="work-tile"><div class="work-photo" role="img" aria-label="Photo of silver jewelry" style="background:radial-gradient(circle at 50% 50%,#8a9ba0 0 26%,#ececea 58%)"></div></div>
      <div class="work-tile"><div class="work-photo" role="img" aria-label="Photo of mixed media artwork" style="background:radial-gradient(circle at 50% 50%,#a88f70 0 32%,#ececea 60%)"></div></div>
    </div>
    <div class="badge"><span class="badge-name">Woven Glass<br>and Tide</span></div>
  </section>

  <section class="card card-back" aria-label="Card back">
    <div class="back-badge"><span class="badge-name">Woven Glass<br>and Tide</span></div>
    <div class="holder">
      <h1 class="holder-name">Helena Pikeworth</h1>
      <p class="holder-role">Designer</p>
      <div class="divider-flourish" role="img" aria-label="Decorative scroll flourish"></div>
    </div>
    <div class="contact">
      <div>
        <p class="contact-line"><b>T</b>604.555.0172</p>
        <p class="contact-line"><b>E</b>Designer@WovenGlassandTide.example</p>
      </div>
      <div>
        <p class="contact-line"><b>W</b>www.WovenGlassandTide.example</p>
        <p class="contact-line"><b>B</b>www.ShapingHillside.example</p>
      </div>
    </div>
  </section>
</main>
</body>
</html>
```